Business Card, Stationary with Shark Logo for Personal Injury Lawyer

I need business cards and stationery with a shark logo for my Personal Injury Law Practice. Has to have this written on it:
Martin K. Hollis
Injury Lawyer
The Corvell Building
718 Tandy Street
Providence, Rhode Island 02908
401-627-4193
Martinhollis.com

Contact Information for Business Card

Martin K. Hollis, Injury Lawyer, address, 401-627-4193, martinhollis.com

```html
<!DOCTYPE html>
<html lang="en">
<head>
<meta charset="utf-8">
<title>Martin K. Hollis – Business Card</title>
<link href="https://fonts.googleapis.com/css2?family=Open+Sans:wght@400;600;800&display=swap" rel="stylesheet">
<style>
  :root {
    --navy: #2a2464;
    --navy-text: #2b2566;
    --teal: #3aa0b8;
    --rule: #9a98c0;
    --paper: #fbfbf9;
    --grey-text: #555a66;
    --backdrop: #e4e3e0;
  }
  * { box-sizing: border-box; margin: 0; padding: 0; }
  html, body {
    width: 1200px; height: 1023px; overflow: hidden;
    background: var(--backdrop);
    font-family: "Open Sans", Arial, sans-serif;
  }
  .canvas {
    position: relative; width: 1200px; height: 1023px;
    display: flex; flex-direction: column; align-items: center; justify-content: center; gap: 90px;
  }
  .card {
    width: 560px; height: 320px;
    position: relative;
    box-shadow: 0 6px 18px rgba(0,0,0,.18);
  }
  .card--front {
    background: var(--navy);
    display: flex; align-items: center; justify-content: center;
  }
  .brand-name {
    font-weight: 800; font-size: 40px; letter-spacing: .5px;
    text-transform: uppercase; color: #ffffff; line-height: 1;
  }
  .card--back {
    background: var(--paper);
    display: flex; align-items: center;
  }
  .card--back .brand-half {
    width: 50%; height: 100%;
    display: flex; align-items: center; justify-content: center;
  }
  .card--back .brand-name { color: var(--navy-text); font-size: 26px; }
  .divider {
    width: 1px; height: 220px; background: var(--rule);
  }
  .contact-half {
    width: 50%; padding-left: 34px; padding-right: 16px;
  }
  .person-name {
    font-weight: 600; font-size: 17px; color: var(--navy-text);
    text-transform: uppercase; letter-spacing: .3px; line-height: 1.2;
  }
  .person-title {
    font-size: 10px; color: var(--grey-text); margin-top: 2px; text-align: right; width: 168px;
  }
  .name-rule {
    width: 130px; height: 1px; background: var(--teal); margin: 6px 0 20px;
  }
  .contact-list { list-style: none; }
  .contact-list li {
    display: flex; align-items: flex-start; gap: 8px;
    font-size: 12px; line-height: 16px; color: var(--grey-text); margin-bottom: 7px;
  }
  .contact-icon { width: 15px; height: 15px; flex: none; margin-top: 1px; }
</style>
</head>
<body>
<main class="canvas">
  <section class="card card--front" aria-label="Card front">
    <p class="brand-name">Martin K. Hollis</p>
  </section>

  <section class="card card--back" aria-label="Card back">
    <div class="brand-half">
      <p class="brand-name">Martin K. Hollis</p>
    </div>
    <div class="divider"></div>
    <div class="contact-half">
      <p class="person-name">Martin K. Hollis</p>
      <p class="person-title">Injury Lawyer</p>
      <div class="name-rule"></div>
      <ul class="contact-list">
        <li>
          <svg class="contact-icon" viewBox="0 0 16 16" aria-hidden="true">
            <circle cx="8" cy="8" r="8" fill="var(--teal)"/>
            <path d="M8 3.5 C5.9 3.5 4.6 5 4.6 6.7 C4.6 9 8 12.6 8 12.6 C8 12.6 11.4 9 11.4 6.7 C11.4 5 10.1 3.5 8 3.5 Z" fill="#fff"/>
            <circle cx="8" cy="6.7" r="1.3" fill="var(--teal)"/>
          </svg>
          <span>The Corvell Building, 718 Tandy Street<br>Providence, Rhode Island 02908</span>
        </li>
        <li>
          <svg class="contact-icon" viewBox="0 0 16 16" aria-hidden="true">
            <circle cx="8" cy="8" r="8" fill="var(--teal)"/>
            <path d="M5.2 4 L6.8 4 L7.4 6 L6.4 6.9 C6.9 8 7.9 9.1 9.1 9.6 L10 8.6 L12 9.2 L12 10.8 C12 11.4 11.5 11.8 10.9 11.8 C7.4 11.6 4.4 8.6 4.2 5.1 C4.2 4.5 4.6 4 5.2 4 Z" fill="#fff"/>
          </svg>
          <span>401-627-4193</span>
        </li>
        <li>
          <svg class="contact-icon" viewBox="0 0 16 16" aria-hidden="true">
            <circle cx="8" cy="8" r="8" fill="var(--teal)"/>
            <rect x="4" y="5" width="8" height="6" fill="none" stroke="#fff" stroke-width="1"/>
            <path d="M4 5 L8 8.5 L12 5" fill="none" stroke="#fff" stroke-width="1"/>
          </svg>
          <span>martin@martinhollis.com</span>
        </li>
        <li>
          <svg class="contact-icon" viewBox="0 0 16 16" aria-hidden="true">
            <circle cx="8" cy="8" r="8" fill="var(--teal)"/>
            <circle cx="8" cy="8" r="4.2" fill="none" stroke="#fff" stroke-width="1"/>
            <ellipse cx="8" cy="8" rx="1.8" ry="4.2" fill="none" stroke="#fff" stroke-width=".9"/>
            <line x1="3.8" y1="8" x2="12.2" y2="8" stroke="#fff" stroke-width=".9"/>
          </svg>
          <span>Martinhollis.com</span>
        </li>
      </ul>
    </div>
  </section>
</main>
</body>
</html>
```